Business Card Design for Orthopaedic Surgeon

This is a double-sided glossy business card. I prefer baby blue, teal, and green as color schemes. I have my logo already (many colors that you can choose from). I have photos and examples of my old card (very bland but has the information in it). I also have one that my assistant tried to design, but the writing is too small and I don't love the formatting. But it is close!
I would like my logo to be on the business card but I'm uploading my logo in many different colors so you can choose which one looks best based on the color scheme. I also uploaded many sized headshots so you can choose the best resolution one.

Additional information:
Correct business address:
4382 NW 58th Lane, Suite 305
Tamarac, FL 33417

Everything else on both business cards are accurate.

I actually need 2 different business cards generated. One that includes my cell phone number-- Personal cell: 585-314-9062 in addition to Office phone: (954) 316-4870 and Office Fax: 954-316-4881. Again, one card would have my personal cell and one wouldn't

Overall I just think the baby blue card (uploaded) is missing something on the front--of course it is also missing my office phone/fax/personal cell. I do want my website on the front too. Email: info@wellsorthocare.example

You can use your discretion about what goes on the front vs. what goes on the back to eliminated clutter.

Oh and on the back, I would like to list "Conditions Treated" (not specialties include). The list is:
Carpal Tunnel
Trigger Finger
Ganglion Cysts
Hand Tumors
Han & Wrist Arthritis
Hand, Wrist & Elbow Tendonitis
Fractures of the Hand, Wrist, Elbow and Humerus
Nerve Injuries of the Hand, Wrist & Elbow
Microsurgery
Wrist Arthroscopy
Endoscopic Surgery

Target Market(s)

Primary care doctors, Lawyers, patients

Industry/Entity Type

Medical

Contact Information for Business Card

Please see above in project description

Colors

Designer to choose colors to be used in the design.

Requirements
Must have
• -Correct office info, Board Certified Orthopaedic Hand & Upper Extremity Surgeon
Nice to have
• Something that is classy and wow!

```html
<!DOCTYPE html>
<html lang="en">
<head>
<meta charset="utf-8">
<title>Renata Wells, M.D. — Business Card</title>
<link href="https://fonts.googleapis.com/css2?family=Montserrat:wght@400;500;600&display=swap" rel="stylesheet">
<style>
  :root {
    --backdrop: #8b7257;
    --card-white: #ffffff;
    --teal: #017f7d;
    --teal-line: #1a8a88;
    --sky-blue: #2a93d5;
    --ink: #1b1b1b;
    --muted-photo: #a9a9a9;
    --gold: #d9b77a;
  }
  * { box-sizing: border-box; margin: 0; padding: 0; }
  html, body { width: 900px; height: 1200px; overflow: hidden; }
  body {
    background: var(--backdrop);
    font-family: "Montserrat", Arial, sans-serif;
    position: relative;
  }
  .card {
    position: absolute;
    left: 80px;
    width: 742px;
    height: 441px;
    border-radius: 30px;
    overflow: hidden;
  }
  .card-front { top: 131px; background: var(--card-white); }
  .card-back { top: 638px; background: var(--teal); }

  .headshot {
    position: absolute; left: 46px; top: 33px;
    width: 183px; height: 210px; border-radius: 22px;
    background: linear-gradient(180deg, #b5b5b5, #8d8d8d);
  }
  .brand {
    position: absolute; right: 60px; top: 120px;
    display: flex; align-items: center; gap: 12px;
    font-weight: 600; font-size: 30px; letter-spacing: 1px;
    text-transform: uppercase;
  }
  .brand-front { color: var(--ink); }
  .brand-mark { width: 24px; height: 24px; border-radius: 50%; background: currentColor; }
  .name {
    position: absolute; left: 38px; top: 264px;
    font-size: 25px; font-weight: 600; color: var(--sky-blue);
  }
  .title {
    position: absolute; left: 37px; top: 296px;
    font-size: 15px; color: var(--teal);
  }
  .rule {
    position: absolute; left: 36px; top: 318px;
    width: 672px; height: 1.5px; background: var(--teal-line);
  }
  .contacts {
    position: absolute; list-style: none;
    font-size: 16px; color: var(--ink); line-height: 23px;
  }
  .contacts li { display: flex; align-items: center; gap: 10px; }
  .contacts-left { left: 38px; top: 335px; }
  .contacts-right { right: 32px; top: 325px; }
  .contacts-right li { justify-content: flex-end; }
  .icon { width: 14px; height: 14px; fill: var(--teal); flex: none; }
  .footer-bands { position: absolute; left: 0; bottom: 0; }
  .address {
    position: absolute; right: 29px; top: 391px;
    color: #fff; font-size: 16px; line-height: 20px; text-align: right;
  }

  .back-heading {
    position: absolute; left: 36px; top: 143px;
    color: #fff; font-size: 24px; font-weight: 500;
  }
  .conditions {
    position: absolute; left: 55px; top: 193px;
    color: #fff; font-size: 16px; line-height: 19.6px;
    list-style: disc;
  }
  .brand-back { color: var(--gold); top: 138px; right: 70px; }
</style>
</head>
<body>

<section class="card card-front">
  <div class="headshot" role="img" aria-label="Portrait photo of Dr. Renata Wells"></div>

  <div class="brand brand-front"><span class="brand-mark"></span>Wells Hand</div>

  <h1 class="name">Renata Wells, M.D.</h1>
  <p class="title">Hand and upper extremity specialist</p>
  <div class="rule"></div>

  <ul class="contacts contacts-left">
    <li><svg class="icon" viewBox="0 0 14 14"><rect x="1" y="5" width="12" height="8" rx="1"/><rect x="3" y="1" width="8" height="3"/></svg>954-316-4881</li>
    <li><svg class="icon" viewBox="0 0 14 14"><path d="M1 3h12v8H1z M1 3l6 4 6-4" /></svg>info@wellsorthocare.example</li>
  </ul>

  <ul class="contacts contacts-right">
    <li>(954) 316-4870<svg class="icon" viewBox="0 0 14 14"><path d="M1 5c0-2 3-3 6-3s6 1 6 3v1h-3V4.5H4V6H1z M3 7h8l1 5H2z"/></svg></li>
    <li>585-314-9062<svg class="icon" viewBox="0 0 14 14"><path d="M4 0h6a1 1 0 0 1 1 1v12a1 1 0 0 1-1 1H4a1 1 0 0 1-1-1V1a1 1 0 0 1 1-1zm0.6 1.5v9h4.8v-9z"/></svg></li>
  </ul>

  <svg class="footer-bands" width="742" height="60" viewBox="0 0 742 60">
    <path d="M0 18 H398 L388 36 H0 Z" fill="#2a93d5"/>
    <path d="M420 0 H742 V60 H0 V36 H392 Q405 36 410 20 Z" fill="#017f7d"/>
  </svg>

  <p class="address">4382 NW 58th Lane, Suite 305<br>Tamarac, FL 33417</p>
</section>

<section class="card card-back">
  <div class="brand brand-back"><span class="brand-mark"></span>Wells Hand</div>
  <h2 class="back-heading">Conditions Treated</h2>
  <ul class="conditions">
    <li>Carpal Tunnel</li>
    <li>Trigger Finger</li>
    <li>Ganglion Cysts</li>
    <li>Hand Tumors</li>
    <li>Han &amp; Wrist Arthritis</li>
    <li>Hand, Wrist &amp; Elbow Tendonitis</li>
    <li>Fractures of the Hand, Wrist, Elbow and Humerus</li>
    <li>Nerve Injuries of the Hand, Wrist &amp; Elbow</li>
    <li>Microsurgery</li>
    <li>Wrist Arthroscopy</li>
    <li>Endoscopic Surgery</li>
  </ul>
</section>

</body>
</html>
```